Healthy Supplement featuring Moringa products

Need 3 business card options for our reps to order from Cardloom. Our reps will be ordering from Cardloom once we upload them. Attached is our current designs to show what info needs to be on the cards. Our website is www.tkvitality.com
The business cards will be a template for our reps to order from. Most of our reps are Asian & Hispanic. Please look at our website so you can see who we are to get the look and feel what we need.
Target Market(s)
Adults 30 on up. Health oriented people.
Industry/Entity Type
Health And Wellness
Contact Information for Business Card
Name
Title
Phone
Logo
www.tkvitality.com/my/username
Font styles to use
Requirements
Must have
- Please match our website look and colors. A moringa leaf is nice, but am open to something different.
Nice to have
- Healthy looking and warm, not super cold or too modern.
Should not have
- No harsh colors please.

```html
<!DOCTYPE html>
<html lang="en">
<head>
<meta charset="utf-8">
<title>TK Vitality – Business Card Options</title>
<link rel="stylesheet" href="https://fonts.googleapis.com/css2?family=Jost:wght@400;500&family=Dosis:wght@500;600&display=swap">
<style>
  :root {
    --stage: #d6d6d6;
    --leaf-dark: #69a942;
    --leaf-light: #93c83e;
    --frame-orange: #ec8c3a;
    --frame-tan: #dcc1a8;
    --frame-copper: #cf7a2c;
    --card-white: #ffffff;
    --ink: #1a1a1a;
  }
  html, body {
    margin: 0;
    padding: 0;
    width: 1200px;
    height: 1200px;
    overflow: hidden;
    background: var(--stage);
  }
  .sheet {
    position: relative;
    width: 1200px;
    height: 1200px;
  }
  .card {
    position: absolute;
    width: 408px;
    height: 264px;
    display: block;
    background: var(--card-white);
    box-shadow: -6px 8px 14px rgba(0, 0, 0, 0.28);
  }
  .card--front-band { left: 124px; top: 280px; }
  .card--back-frame { left: 658px; top: 280px; }
  .card--front-chevron { left: 124px; top: 646px; }
  .card--back-logo { left: 658px; top: 646px; }

  .fill-dark { fill: var(--leaf-dark); }
  .fill-light { fill: var(--leaf-light); }
  .fill-white { fill: var(--card-white); }

  .brand-name {
    font-family: "Jost", sans-serif;
    font-weight: 500;
    fill: var(--leaf-dark);
    letter-spacing: 0.04em;
  }
  .contact-green {
    font-family: "Dosis", sans-serif;
    font-weight: 600;
    font-size: 15px;
    fill: var(--leaf-dark);
    letter-spacing: 0.06em;
  }
  .contact-ink {
    font-family: "Jost", sans-serif;
    font-weight: 400;
    font-size: 15px;
    fill: var(--ink);
    letter-spacing: 0.08em;
  }
  .site-small {
    font-family: "Dosis", sans-serif;
    font-weight: 600;
    font-size: 7.5px;
    fill: var(--leaf-dark);
  }
  .icon-line {
    fill: none;
    stroke: var(--leaf-dark);
    stroke-width: 1.4;
  }
  .frame-line {
    fill: none;
    stroke: url(#frameGradient);
    stroke-width: 3;
  }
</style>
</head>
<body>
<main class="sheet">

  <svg width="0" height="0" style="position:absolute" aria-hidden="true">
    <defs>
      <linearGradient id="frameGradient" x1="0" y1="0" x2="1" y2="0">
        <stop offset="0" stop-color="#ec8c3a"/>
        <stop offset="0.55" stop-color="#e9a56a"/>
        <stop offset="0.8" stop-color="#dcc1a8"/>
        <stop offset="1" stop-color="#cf7a2c"/>
      </linearGradient>
    </defs>
  </svg>

  <!-- Option 1: front with angled bands -->
  <svg class="card card--front-band" viewBox="0 0 510 330">
    <rect class="fill-white" width="510" height="330"/>
    <polygon class="fill-dark" points="0,0 260,0 325,197 67,197"/>
    <polygon class="fill-light" points="390,0 510,0 442,197 325,197"/>
    <text class="brand-name" x="103" y="270" font-size="22" text-anchor="middle">TK Vitality</text>

    <g class="contact-list">
      <path class="fill-dark" d="M282,238 c2,-2 4,-2 5,0 l1,2 c0,1 -1,2 -2,2 c1,2 2,3 4,4 c0,-1 1,-2 2,-2 l2,1 c2,1 2,3 0,5 c-5,1 -13,-6 -12,-12z"/>
      <text class="contact-green" x="310" y="247">(555) 214-3870</text>

      <rect class="icon-line" x="281" y="263" width="15" height="10"/>
      <polyline class="icon-line" points="281,263 288.5,269 296,263"/>
      <text class="contact-green" x="310" y="271">info@tkvitality.com</text>

      <circle class="icon-line" cx="288.5" cy="289" r="7"/>
      <ellipse class="icon-line" cx="288.5" cy="289" rx="3" ry="7"/>
      <line class="icon-line" x1="281.5" y1="289" x2="295.5" y2="289"/>
      <text class="contact-green" x="310" y="295">www.tkvitality.com</text>
    </g>
  </svg>

  <!-- Option 1: back with frame and contacts -->
  <svg class="card card--back-frame" viewBox="0 0 510 330">
    <rect class="fill-white" width="510" height="330"/>
    <rect class="frame-line" x="23" y="21" width="464" height="289"/>
    <polygon class="fill-light" points="0,0 98,0 0,98"/>
    <polygon class="fill-dark" points="510,232 510,330 412,330"/>
    <text class="brand-name" x="255" y="118" font-size="26" text-anchor="middle">TK Vitality</text>
    <text class="contact-ink" x="255" y="216" text-anchor="middle">(555) 214-3870</text>
    <text class="contact-ink" x="255" y="240" text-anchor="middle">info@tkvitality.com</text>
    <text class="contact-ink" x="255" y="263" text-anchor="middle">www.tkvitality.com</text>
  </svg>

  <!-- Option 2: chevron front -->
  <svg class="card card--front-chevron" viewBox="0 0 510 330">
    <rect class="fill-dark" width="510" height="330"/>
    <polygon class="fill-white" points="0,0 260,0 325,188 275,330 115,330"/>
    <polygon class="fill-light" points="390,0 510,0 395,330 275,330"/>
    <text class="brand-name" x="184" y="180" font-size="26" text-anchor="middle">TK Vitality</text>
    <text class="site-small" x="184" y="219" text-anchor="middle">www.tkvitality.com</text>
  </svg>

  <!-- Option 2: framed logo back -->
  <svg class="card card--back-logo" viewBox="0 0 510 330">
    <rect class="fill-white" width="510" height="330"/>
    <rect class="frame-line" x="24" y="21" width="464" height="288"/>
    <polygon class="fill-light" points="0,0 162,0 0,162"/>
    <polygon class="fill-dark" points="510,172 510,330 350,330"/>
    <text class="brand-name" x="258" y="175" font-size="38" text-anchor="middle">TK Vitality</text>
  </svg>

</main>
</body>
</html>
```